Executive recruiting firm in need of business card design

Executive recruiting firm looking for a sleek, classy and modern business card design; card itself will be square shape, rounded edges and soft touch paper, our colors are dark blues in the navy color scale, silvers and grays. Reference our website for a better idea of our company's feel and goals at Staffvex.com - our company message is "Employee Engagement Begins at Recruitment" this should be on the card

Industry/Entity Type

Business

```html
<!DOCTYPE html>
<html lang="en">
<head>
<meta charset="utf-8">
<title>Staffvex Business Card</title>
<link href="https://fonts.googleapis.com/css2?family=Raleway:wght@300;400&display=swap" rel="stylesheet">
<style>
  :root {
    --navy: #17154a;
    --white: #ffffff;
    --silver: #9a9bb0;
    --gray: #6d6e7e;
    --backdrop: #e6e7ec;
  }
  * { margin: 0; padding: 0; box-sizing: border-box; }
  html, body { width: 1200px; height: 786px; overflow: hidden; }
  body {
    background: var(--backdrop);
    font-family: "Raleway", Arial, sans-serif;
    font-weight: 300;
    display: flex;
    align-items: center;
    justify-content: center;
    gap: 60px;
  }
  .card {
    width: 520px;
    height: 298px;
    border-radius: 10px;
    position: relative;
    box-shadow: 0 6px 18px rgba(23, 21, 74, 0.18);
    overflow: hidden;
  }
  .card--front { background: var(--navy); color: var(--white); }
  .card--back { background: var(--white); color: var(--navy); }

  .company { position: absolute; font-weight: 400; line-height: 1; white-space: nowrap; }
  .company__sub { position: absolute; font-size: 10px; color: var(--silver); white-space: nowrap; }

  .card--front .company { left: 0; right: 0; top: 100px; text-align: center; font-size: 40px; }
  .card--front .company__sub { left: 0; right: 0; top: 150px; text-align: center; font-size: 11px; }
  .tagline {
    position: absolute; left: 0; right: 0; top: 206px;
    text-align: center; font-size: 14px; letter-spacing: 0.02em; color: var(--silver);
  }

  .card--back .company { left: 40px; top: 84px; font-size: 36px; }
  .card--back .company__sub { left: 41px; top: 128px; font-size: 11px; color: var(--gray); }
  .divider { position: absolute; left: 272px; top: 72px; width: 1px; height: 110px; background: var(--navy); }
  .contact { position: absolute; left: 290px; top: 76px; }
  .contact__name { font-size: 17px; font-weight: 400; color: var(--navy); }
  .contact__role { font-size: 12px; color: var(--gray); margin-top: 2px; margin-bottom: 10px; }
  .contact__line { display: flex; align-items: center; gap: 8px; font-size: 11.5px; color: var(--gray); margin-top: 5px; }
  .contact__line svg { width: 11px; height: 11px; flex: none; }
  .address { position: absolute; left: 40px; top: 228px; font-size: 12px; color: var(--gray); letter-spacing: 0.02em; }
</style>
</head>
<body>
  <section class="card card--front">
    <p class="company">Staffvex</p>
    <p class="company__sub">talent acquisition</p>
    <p class="tagline">Employee Engagement Begins at Recruitment</p>
  </section>

  <section class="card card--back">
    <p class="company">Staffvex</p>
    <p class="company__sub">talent acquisition</p>
    <span class="divider"></span>
    <div class="contact">
      <p class="contact__name">Marianne Holt</p>
      <p class="contact__role">Founder</p>
      <p class="contact__line">
        <svg viewBox="0 0 12 12" aria-hidden="true"><path d="M3 1 L5 3.5 L4 5 Q5 7 7 8 L8.5 7 L11 9 L9.5 11 Q4 10.5 1 3 Z" fill="var(--navy)"/></svg>
        +1.212.555.0148
      </p>
      <p class="contact__line">
        <svg viewBox="0 0 12 12" aria-hidden="true"><rect x="3" y="0.5" width="6" height="11" rx="1" fill="none" stroke="var(--navy)"/><rect x="5" y="9" width="2" height="1" fill="var(--navy)"/></svg>
        917-555-0193
      </p>
      <p class="contact__line">
        <svg viewBox="0 0 12 12" aria-hidden="true"><rect x="0.5" y="2" width="11" height="8" fill="var(--navy)"/><path d="M0.5 2 L6 6.5 L11.5 2" fill="none" stroke="var(--white)"/></svg>
        mholt@staffvex.com
      </p>
    </div>
    <p class="address">118 Harbor Street Suite # 410 Riverton NY 10002</p>
  </section>
</body>
</html>
```